Hi, Looking for an upgraded business card to the aged one attached. Open to suggestions and no real limitations, but if your going to use a picture of a taxi i think it should be vector based rather than a full color picture. I've uploaded a 2 pictures of the type of taxi which is a Velmora K7 in white. The taxi markings look like the pink one in the picture but to be clear his is white. The taxi is in Bermuda so if you wanted to include something island based that's ok as well but not required. The other thing he wanted to keep on there was the bermuda police crest, with the retired police office incorporated somehow.

Requirements
Must have
• Bermuda Taxi Operator
Retired Police Officer
Police Crest
Taxi #
Email
Mobile Number

```html
<!DOCTYPE html>
<html lang="en">
<head>
<meta charset="utf-8">
<title>Bermuda Taxi Operator – Business Card</title>
<link rel="stylesheet" href="https://fonts.googleapis.com/css2?family=Oswald:wght@700&family=Montserrat:wght@600&family=Didact+Gothic&display=swap">
<style>
  :root {
    --backdrop: #737373;
    --taxi-yellow: #ffcc00;
    --ink: #2b2b2b;
    --paper: #ffffff;
    --crest-navy: #1a4f8b;
    --card-edge: #d6d6d6;
  }
  * { margin: 0; padding: 0; box-sizing: border-box; }
  html, body {
    width: 1200px;
    height: 793px;
    overflow: hidden;
    background: var(--backdrop);
  }
  .business-card {
    position: absolute;
    left: 143px;
    top: 124px;
    width: 913px;
    height: 546px;
    background: var(--paper);
    outline: 1px solid var(--card-edge);
  }
  .brand-panel {
    position: absolute;
    left: 0;
    top: 0;
    width: 509px;
    height: 100%;
    background: var(--taxi-yellow);
  }
  .brand-pointer {
    position: absolute;
    left: 509px;
    top: 234px;
    width: 34px;
    height: 67px;
  }
  .brand-title {
    position: absolute;
    left: 0;
    top: 140px;
    width: 509px;
    text-align: center;
    font-family: "Oswald", sans-serif;
    font-weight: 700;
    color: var(--ink);
    text-transform: uppercase;
  }
  .brand-title span { display: block; }
  .brand-title__region { font-size: 60px; line-height: 66px; letter-spacing: 0.5px; }
  .brand-title__service { font-size: 140px; line-height: 138px; letter-spacing: 1px; }
  .brand-title__role { font-size: 57px; line-height: 62px; letter-spacing: 0.5px; }

  .agency-mark {
    position: absolute;
    right: 36px;
    top: 44px;
    display: flex;
    align-items: center;
    gap: 10px;
    font-family: "Montserrat", sans-serif;
    font-weight: 600;
    font-size: 14px;
    line-height: 17px;
    color: var(--crest-navy);
  }
  .agency-mark__dot {
    width: 54px;
    height: 54px;
    border-radius: 50%;
    background: var(--crest-navy);
    flex: none;
  }

  .operator-details {
    position: absolute;
    left: 553px;
    top: 248px;
    color: var(--ink);
  }
  .operator-name {
    font-family: "Montserrat", sans-serif;
    font-weight: 600;
    font-size: 39px;
    line-height: 44px;
  }
  .operator-rank {
    font-family: "Didact Gothic", sans-serif;
    font-size: 22px;
    line-height: 28px;
    margin-top: 2px;
  }
  .operator-contact {
    margin-top: 24px;
    font-family: "Didact Gothic", sans-serif;
    font-size: 21px;
    line-height: 29px;
  }
  .operator-phone {
    font-family: "Montserrat", sans-serif;
    font-weight: 600;
    font-size: 32px;
    line-height: 40px;
    margin-top: 2px;
  }
</style>
</head>
<body>
  <div class="business-card">
    <div class="brand-panel">
      <h1 class="brand-title">
        <span class="brand-title__region">Bermuda</span>
        <span class="brand-title__service">Taxi</span>
        <span class="brand-title__role">Operator</span>
      </h1>
    </div>
    <svg class="brand-pointer" viewBox="0 0 34 67" aria-hidden="true">
      <polygon points="0,0 34,33.5 0,67" fill="var(--taxi-yellow)"/>
    </svg>

    <div class="agency-mark">
      <span class="agency-mark__dot" aria-hidden="true"></span>
      <span>Harbour<br>Constabulary</span>
    </div>

    <div class="operator-details">
      <p class="operator-name">Dorian Vessey</p>
      <p class="operator-rank">Retired Police Officer</p>
      <div class="operator-contact">
        <p class="operator-taxi">Taxi #T2719</p>
        <p class="operator-email">dvessey48@mailbox.com</p>
      </div>
      <p class="operator-phone">1-441-555-0147</p>
    </div>
  </div>
</body>
</html>
```